Motivational Poster Design Project

I would like to create a poster with some of my favorite quotes to hang in my office.

Industry/Entity Type

Quotes

Requirements
Must have
• The poster will be 24" high x 36" long and printed on canvas, so the image you create needs to have a resolution of at least 2700 x 3900.

The poster must contain the following quotes:

“Your beliefs become your thoughts,
Your thoughts become your words,
Your words become your actions,
Your actions become your habits,
Your habits become your values,
Your values become your destiny.”
-Varuna Pellath

"Winners practice until they get it right. Champions practice until they can’t get it wrong!"
-Unknown

"Style is the perfection of a point of view."
-Conrad Whitlowe

"My interest in life comes from setting myself huge, apparently unachieveable challenges and trying to rise above them."
-Sir Oswin Talbrook

"Problems cannot be solved by the same level of thinking that created them."
-Gustav Morrendel

"People think focus means saying yes to the thing you've got to focus on. But that's not what it means at all. It means saying no to the hundred other good ideas that there are. You have to pick carefully."
-Dale Parrick

"Think like a man of action and act like a man of thought."
-Lucien Marvaud
Nice to have
• It would be nice to have an image of each person who is being quoted (if known) along with the quote that is attributable to them.

```html
<!DOCTYPE html>
<html lang="en">
<head>
<meta charset="utf-8">
<title>Quotes Poster</title>
<link rel="stylesheet" href="https://fonts.googleapis.com/css2?family=Yellowtail&display=swap">
<style>
  :root {
    --sky-top: #0f5a8f;
    --sky-mid: #2aa6c8;
    --horizon: #7fd2dc;
    --sea: #1fb8a8;
    --sea-deep: #0d8f86;
    --shallows: #8fd6c6;
    --sand: #d9d4cc;
    --sand-light: #ebe7e1;
    --quote-light: #c6ecef;
    --quote-muted: #a6c9c9;
    --shadow-dark: rgba(20, 40, 50, 0.75);
    --portrait-light: #b9b2a8;
    --portrait-dark: #3d3f48;
  }
  html, body {
    margin: 0;
    padding: 0;
    overflow: hidden;
    background: #ffffff;
  }
  .poster {
    position: relative;
    width: 1200px;
    height: 800px;
    overflow: hidden;
    font-family: "Yellowtail", cursive;
  }
  .scene {
    position: absolute;
    inset: 0;
    width: 1200px;
    height: 800px;
  }
  .portrait {
    position: absolute;
    border-radius: 50%;
    background: radial-gradient(ellipse at center, var(--portrait-light) 0%, var(--portrait-dark) 55%, rgba(40, 44, 52, 0) 72%);
  }
  .portrait--mono {
    background: radial-gradient(ellipse at center, #bdbdbd 0%, #4a4a4a 55%, rgba(60, 60, 60, 0) 72%);
  }
  .quote {
    position: absolute;
    margin: 0;
    font-size: 21px;
    line-height: 30px;
    color: var(--quote-light);
    text-shadow: 1px 1px 2px var(--shadow-dark);
    white-space: nowrap;
  }
  .quote--muted {
    color: var(--quote-muted);
    text-shadow: 0 0 1px #2c3e44, 1px 1px 2px var(--shadow-dark);
  }
  .quote--right {
    text-align: right;
  }
  .quote cite {
    display: block;
    font-style: normal;
  }
  .quote__line {
    display: block;
  }
</style>
</head>
<body>
<main class="poster">
  <svg class="scene" viewBox="0 0 1200 800" role="img" aria-label="Tropical beach with turquoise sea, distant karst islands, clouds and a moored longtail boat on white sand">
    <defs>
      <linearGradient id="beach" x1="0" y1="0" x2="0" y2="1">
        <stop offset="0" stop-color="var(--sky-top)"/>
        <stop offset="0.28" stop-color="var(--sky-mid)"/>
        <stop offset="0.41" stop-color="var(--horizon)"/>
        <stop offset="0.43" stop-color="var(--sea-deep)"/>
        <stop offset="0.58" stop-color="var(--sea)"/>
        <stop offset="0.70" stop-color="var(--shallows)"/>
        <stop offset="0.80" stop-color="var(--sand)"/>
        <stop offset="1" stop-color="var(--sand-light)"/>
      </linearGradient>
    </defs>
    <rect width="1200" height="800" fill="url(#beach)"/>
  </svg>

  <div class="portrait" style="left:272px;top:72px;width:96px;height:130px" role="img" aria-label="Portrait of Sir Oswin Talbrook"></div>
  <div class="portrait portrait--mono" style="left:624px;top:146px;width:86px;height:102px" role="img" aria-label="Portrait of Gustav Morrendel"></div>
  <div class="portrait" style="left:686px;top:342px;width:84px;height:120px" role="img" aria-label="Portrait of Varuna Pellath"></div>
  <div class="portrait" style="left:84px;top:444px;width:82px;height:108px" role="img" aria-label="Portrait of Conrad Whitlowe"></div>
  <div class="portrait portrait--mono" style="left:874px;top:526px;width:86px;height:102px" role="img" aria-label="Portrait of Lucien Marvaud"></div>
  <div class="portrait portrait--mono" style="left:1066px;top:652px;width:104px;height:126px" role="img" aria-label="Portrait of Dale Parrick"></div>

  <blockquote class="quote" style="left:30px;top:24px">
    <span class="quote__line">"My interest in life comes from setting myself huge, apparently unachieveable challenges and trying to rise above them."</span>
    <cite>- Sir Oswin Talbrook</cite>
  </blockquote>

  <blockquote class="quote quote--right" style="right:40px;top:116px">
    <span class="quote__line">"Problems cannot be solved by the same level of thinking that created them."</span>
    <cite>-Gustav Morrendel</cite>
  </blockquote>

  <blockquote class="quote quote--right" style="right:62px;top:214px">
    <span class="quote__line">“Your beliefs become your thoughts,</span>
    <span class="quote__line">Your thoughts become your words,</span>
    <span class="quote__line">Your words become your actions,</span>
    <span class="quote__line">Your actions become your habits,</span>
    <span class="quote__line">Your habits become your values,</span>
    <span class="quote__line">Your values become your destiny.”</span>
    <cite>- Varuna Pellath</cite>
  </blockquote>

  <blockquote class="quote" style="left:22px;top:240px">
    <span class="quote__line">"Winners practice until they get it right.</span>
    <span class="quote__line">Champions practice until they can't get it wrong!"</span>
    <cite>- Unknown</cite>
  </blockquote>

  <blockquote class="quote quote--right" style="right:48px;top:486px">
    <span class="quote__line">"Think like a man of action and act like a man of thought."</span>
    <cite>- Lucien Marvaud</cite>
  </blockquote>

  <blockquote class="quote quote--muted" style="left:30px;top:574px">
    <span class="quote__line">"Style is the perfection of a point of view."</span>
    <cite>- Conrad Whitlowe</cite>
  </blockquote>

  <blockquote class="quote quote--muted quote--right" style="right:128px;top:652px;line-height:33px">
    <span class="quote__line">"People think focus means saying yes to the thing you've got to focus on.</span>
    <span class="quote__line">But that's not what it means at all. It means saying no to the hundred other good ideas that there are.</span>
    <span class="quote__line">You have to pick carefully."</span>
    <cite style="margin-right:32px;line-height:26px">- Dale Parrick</cite>
  </blockquote>
</main>
</body>
</html>
```